QUOTE Graphics for Summer Challenge

I would like to put these quotes over one of the pictures attached; For Instagram, use new size: 4:5 (1080 x 1350 pixels). One Quote per picture, and I want the quote to be bold or easy to read as well. I provided a few reference graphics that I really like as examples below.
All of the pictures are attached; you can pick any photo and add one quote to it; but no stock photography
All the quotes are in the attached WORD document

```html
<!DOCTYPE html>
<html lang="en">
<head>
<meta charset="utf-8">
<title>Glow Girl Summer Slimdown – Quote Graphics</title>
<link href="https://fonts.googleapis.com/css2?family=Bebas+Neue&family=Lato:ital,wght@0,400;0,700;0,900;1,400&family=Oswald:wght@300&display=swap" rel="stylesheet">
<style>
:root{
  --canvas:#262427;
  --plum:#8a4f86;
  --plum-deep:#6f3a6d;
  --plum-light:#a56aa0;
  --rose:#f2707c;
  --white:#ffffff;
}
*{margin:0;padding:0;box-sizing:border-box}
html,body{width:1200px;height:904px;overflow:hidden;background:var(--canvas)}
.board{position:relative;width:1200px;height:904px}
.post{position:absolute;overflow:hidden;color:var(--white);font-family:'Lato',sans-serif}
.post .photo{position:absolute;inset:0}
.photo-a{background:linear-gradient(160deg,var(--plum-light) 0%,var(--plum) 45%,var(--plum-deep) 100%)}
.photo-b{background:linear-gradient(200deg,#9a5f96 0%,var(--plum) 50%,#7b4478 100%)}
.photo-c{background:linear-gradient(180deg,#7e4579 0%,#965a90 60%,#8a4f86 100%)}
.post > *:not(.photo){position:absolute}
.display{font-family:'Bebas Neue',sans-serif;font-weight:400;text-transform:uppercase}
.thin{font-family:'Oswald',sans-serif;font-weight:300;text-transform:uppercase}
.handle{font-family:'Lato',sans-serif;font-style:italic;font-size:6px;left:11px;top:245px}
.rule{height:2px;background:var(--white)}
.rose-rule{background:var(--rose)}
.tag{background:var(--rose);color:var(--white);padding:0 3px}
.col1{left:516px}.col2{left:740px}.col3{left:965px}
.row1{top:46px}.row2{top:322px}.row3{top:597px}
.small{width:209px;height:260px}

/* hero */
.hero{left:35px;top:46px;width:462px;height:579px}
.hero .intro{left:24px;top:18px;font-weight:700;font-size:27px;line-height:32px;letter-spacing:-.3px}
.hero .shout{left:21px;top:166px;font-size:106px;line-height:90px;letter-spacing:3px}
.hero .cta{left:24px;top:447px;font-size:23px;line-height:27px;font-weight:400}
.hero .handle{left:24px;top:541px;font-size:12px}

.b b,.bold{font-weight:900}
</style>
</head>
<body>
<main class="board">

  <!-- hero post -->
  <section class="post hero">
    <div class="photo photo-a" role="img" aria-label="Photo of the coach standing poolside in a sheer knit maxi dress, tinted plum"></div>
    <p class="intro">We’re getting a<br>tiny waist and<br>dropping pounds<br>together.</p>
    <p class="display shout">Don’t<br>Miss<br>This</p>
    <p class="cta">COMMENT GLOW<br>GIRL TO JOIN</p>
    <p class="handle">@AvaLaneOnline</p>
  </section>

  <!-- motivation -->
  <section class="post small col1 row1">
    <div class="photo photo-b" role="img" aria-label="Photo of the coach posing in a knit dress by the pool, tinted plum"></div>
    <p class="thin" style="left:11px;top:7px;font-size:20px;line-height:22px">You<br>Don’t need<br>motivation.</p>
    <div class="rule" style="left:11px;top:80px;width:33px"></div>
    <p class="display" style="left:11px;top:88px;font-size:27px;line-height:24px">You need a<br>proven plan<br>and some<br>accountability</p>
    <p style="left:11px;top:200px;font-size:8.5px">Comment <b>GLOW GIRL</b> to</p>
    <p class="tag" style="left:11px;top:213px;font-size:7.5px;line-height:14px">GET JOIN US ON JULY 7</p>
    <p class="handle">@AvaLaneOnline</p>
  </section>

  <!-- summer here -->
  <section class="post small col2 row1">
    <div class="photo photo-c" role="img" aria-label="Photo of the coach sitting at the pool edge in a leopard swimsuit, tinted plum"></div>
    <p class="display" style="left:22px;top:10px;font-size:64px;line-height:60px">Summer</p>
    <p class="display" style="left:23px;top:64px;font-size:50px;line-height:42px">Here</p>
    <p style="left:106px;top:65px;font-size:10px;line-height:12.5px">BUT YOUR BODY<br>DOESN’T FEEL<br>READY?</p>
    <p class="display" style="left:11px;top:130px;font-size:23px;line-height:19.5px">You’re<br>not too<br>late.</p>
    <p style="right:9px;top:129px;font-size:10px;line-height:12.7px;text-align:right">Comment<br>SUMMER<br>to join the<br><b class="bold">Glow Girl<br>Summer<br>Slimdown</b></p>
    <p class="handle" style="left:auto;right:9px;top:247px">@AvaLaneOnline</p>
  </section>

  <!-- belly bloat -->
  <section class="post small col3 row1">
    <div class="photo photo-b" role="img" aria-label="Photo of the coach in a crochet dress, tinted plum"></div>
    <p class="display" style="left:11px;top:12px;font-size:16px;line-height:14px">Your belly bloat<br>and stubborn<br>weight gain aren’t<br>going anywhere...</p>
    <p class="display" style="left:11px;top:84px;font-size:28px;line-height:24px">Unless<br>you do<br>something<br>different.</p>
    <p style="left:11px;top:196px;font-size:9px">Comment GLOW GIRL to</p>
    <p style="left:11px;top:207px;font-size:17px;font-weight:700">JOIN US!</p>
    <p class="handle">@AvaLaneOnline</p>
  </section>

  <!-- jumpstart -->
  <section class="post small col1 row2">
    <div class="photo photo-c" role="img" aria-label="Photo of the coach in sunglasses and a black swimsuit in the pool, tinted plum"></div>
    <p style="left:11px;top:11px;font-size:10.5px;line-height:11.5px;font-weight:700">IF YOU FEEL<br>LIKE YOU’VE LET<br>YOURSELF GO LATELY,</p>
    <p class="display" style="left:11px;top:60px;font-size:25px;line-height:22px">This is your</p>
    <p class="display" style="left:11px;top:80px;font-size:35px;line-height:30px">Jumpstart</p>
    <div class="rule rose-rule" style="left:11px;top:120px;width:22px"></div>
    <p style="left:11px;top:130px;font-size:10.5px;line-height:12.5px">COMMENT<br><b>SUMMER</b><br>TO JOIN THE</p>
    <p class="display" style="left:11px;top:172px;font-size:22px;line-height:17px">Glow Girl<br>Summer<br>Slimdown</p>
    <p class="handle">@AvaLaneOnline</p>
  </section>

  <!-- need a jumpstart -->
  <section class="post small col2 row2">
    <div class="photo photo-a" role="img" aria-label="Photo of the coach in a crochet outfit outdoors, tinted plum"></div>
    <p class="display" style="left:12px;top:64px;font-size:29px;line-height:26px">Need a</p>
    <p class="display" style="left:10px;top:88px;font-size:53px;line-height:46px">Jumpstart?</p>
    <p class="display" style="left:0;width:209px;top:144px;font-size:22px;line-height:20px;text-align:center">We’re detoxing,<br>burning fat, and<br>getting snatched.</p>
    <p style="left:0;width:209px;top:213px;font-size:8.5px;line-height:10px;font-weight:700;text-align:center">COMMENT GLOW GIRL TO<br>JOIN US ON JULY 7TH</p>
    <p class="handle" style="left:0;width:209px;top:244px;text-align:center">@AvaLaneOnline</p>
  </section>

  <!-- cravings -->
  <section class="post small col3 row2">
    <div class="photo photo-b" role="img" aria-label="Photo of the coach in sunglasses and a swimsuit at the pool edge, tinted plum"></div>
    <p class="display" style="left:10px;top:8px;font-size:24px;line-height:21.7px">Cravings<br>belly fat<br>and water<br>weight?</p>
    <div class="rule" style="left:11px;top:110px;width:104px;height:1.5px"></div>
    <p class="thin" style="left:10px;top:115px;font-size:16px;line-height:18px">Say goodbye in</p>
    <p class="display" style="left:10px;top:131px;font-size:45px;line-height:40px">30 Days</p>
    <div class="rule" style="left:11px;top:171px;width:108px;height:1.5px"></div>
    <p style="left:12px;top:182px;font-size:10px;line-height:12.7px">Comment <b>SUMMER</b><br>to join the <b>Glow Girl<br>Summer Slimdown</b></p>
    <p class="handle">@AvaLaneOnline</p>
  </section>

  <!-- detox -->
  <section class="post small col1 row3">
    <div class="photo photo-a" role="img" aria-label="Photo of the coach smiling in a leopard swimsuit, tinted plum"></div>
    <p class="display" style="left:13px;top:14px;font-size:24px;line-height:21px">Feeling<br>bloated,<br>sluggish,<br>and too big?</p>
    <div style="left:14px;top:106px;width:181px;height:79px;border:1px solid var(--white)"></div>
    <p class="display" style="left:14px;width:181px;top:112px;font-size:40px;line-height:33px;text-align:center">Your detox<br>starts now</p>
    <p style="left:0;width:209px;top:192px;font-size:11px;line-height:12px;font-weight:700;text-align:center">COMMENT SUMMER TO JOIN THE<br>GLOW GIRL SUMMER<br>SLIMDOWN</p>
    <p class="handle" style="left:0;width:209px;top:248px;text-align:center">@AvaLaneOnline</p>
  </section>

  <!-- lifeline -->
  <section class="post small col2 row3">
    <div class="photo photo-c" role="img" aria-label="Photo of the coach in a black swimsuit standing in the pool, tinted plum"></div>
    <p class="display" style="left:10px;top:13px;font-size:17px;line-height:15px">The scale<br>keeps climbing<br>and nothing’s<br>working?</p>
    <p class="display" style="left:10px;top:85px;font-size:29px;line-height:25.5px;color:var(--rose)">This<br>challenge<br>is your<br>lifeline.</p>
    <p style="left:10px;top:193px;font-size:7.5px">COMMENT GLOW GIRL TO</p>
    <p class="tag" style="left:10px;top:204px;font-size:13px;line-height:15px">JOIN NOW!</p>
    <p class="handle" style="top:247px">@AvaLaneOnline</p>
  </section>

  <!-- slimdown -->
  <section class="post small col3 row3">
    <div class="photo photo-b" role="img" aria-label="Photo of the coach in a knit dress by the infinity pool, tinted plum"></div>
    <p class="display" style="right:8px;top:9px;font-size:36px;line-height:31px;text-align:right">Glow Girl</p>
    <p class="display" style="right:8px;top:37px;font-size:51px;line-height:44px;text-align:right">Summer</p>
    <p class="display" style="right:8px;top:82px;font-size:28px;line-height:25px;text-align:right">Slimdown</p>
    <p style="right:8px;top:117px;font-size:10.5px;line-height:12px;text-align:right">plan is helping<br>women drop pounds<br>and feel sexy again.</p>
    <div style="left:130px;top:171px;width:69px;height:49px;border:1px solid var(--white)"></div>
    <p style="left:130px;width:69px;top:175px;font-size:8.5px;line-height:10.5px;text-align:center">COMMENT<br>SUMMER TO<br><span style="font-size:14px;line-height:16px">JOIN US</span></p>
    <p class="handle" style="left:auto;right:11px;top:247px;font-style:normal;font-size:5.5px">@AvaLaneOnline</p>
  </section>

</main>
</body>
</html>
```